Painting Company Business Card

Brightwell Painting needs a new business card. See attachments for our logo and current card as an example.
We want to utilize the same colors in the logo, and keep all the information that is currently on it. Just need an updated and modern design.
We are open to loosing the Association Logos if it means a better design.
We are also entertaining a spot for a picture of a headshot of the person listed on the card. Head shot can be finished later.

```html
<!DOCTYPE html>
<html lang="en">
<head>
<meta charset="utf-8">
<title>Brightwell Painting – Business Card</title>
<link rel="stylesheet" href="https://fonts.googleapis.com/css2?family=Source+Sans+3:ital,wght@0,400;0,600;0,700;1,700&display=swap">
<style>
  :root {
    --backdrop: #3b3b3c;
    --card-white: #ffffff;
    --forest: #343f33;
    --brick: #6a3c36;
    --text-light: #ffffff;
    --badge-blue: #2f5f9e;
    --badge-grey: #9a9a9a;
    --badge-red: #b5322e;
  }
  * { box-sizing: border-box; margin: 0; padding: 0; }
  html, body {
    width: 1200px; height: 486px; overflow: hidden;
    background: var(--backdrop);
    font-family: "Source Sans 3", "Myriad Pro", Arial, sans-serif;
  }
  .canvas { position: relative; width: 1200px; height: 486px; }
  .card {
    position: absolute; top: 86px; width: 503px; height: 325px;
    background: var(--card-white); overflow: hidden;
  }
  .card--front { left: 63px; }
  .card--back { left: 637px; }
  .card__edge { position: absolute; inset: 0; width: 100%; height: 100%; }

  .brand {
    position: absolute; left: 22px; top: 34px;
    color: var(--forest); font-weight: 700;
    font-size: 46px; line-height: 0.98; letter-spacing: -0.5px;
  }
  .person { position: absolute; left: 270px; top: 58px; width: 230px; text-align: center; }
  .person__name { color: var(--forest); font-weight: 700; font-size: 27px; line-height: 1.2; }
  .person__role { color: var(--brick); font-weight: 400; font-size: 26px; line-height: 1.25; }

  .contact {
    position: absolute; left: 0; right: 0; top: 218px;
    text-align: center; color: var(--text-light);
    font-size: 21px; line-height: 29px; padding-left: 18px;
  }

  .services {
    position: absolute; left: 0; right: 0; top: 38px;
    text-align: center; color: var(--text-light);
    font-style: italic; font-weight: 700; font-size: 28px; line-height: 36px;
  }
  .website {
    position: absolute; left: 0; right: 0; top: 194px;
    text-align: center; color: var(--brick); font-size: 24px;
  }
  .memberships {
    position: absolute; left: 40px; right: 14px; top: 244px; height: 64px;
    display: flex; align-items: center; justify-content: space-between;
  }
  .badge { display: block; }
</style>
</head>
<body>
<main class="canvas">

  <section class="card card--front" aria-label="Business card front">
    <svg class="card__edge" viewBox="0 0 503 325" preserveAspectRatio="none" aria-hidden="true">
      <path fill="var(--forest)" d="M0,190 L14,184 L30,187 L44,178 L62,182 L80,176 L96,181 L114,174 L130,179 L150,172 L168,178 L186,170 L204,176 L222,169 L240,174 L258,166 L278,172 L300,167 L318,174 L336,168 L356,172 L372,163 L392,168 L410,158 L428,164 L446,152 L462,160 L478,150 L492,158 L503,154 L503,325 L0,325 Z"/>
    </svg>
    <div class="brand">Brightwell<br>Painting</div>
    <div class="person">
      <p class="person__name">Daniel Morris</p>
      <p class="person__role">Quality Manager</p>
    </div>
    <div class="contact">
      <p class="contact__phone">262-555-0148</p>
      <p class="contact__email">Daniel.Brightwell@mailbox.com</p>
      <p class="contact__web">BrightwellPainting.com</p>
    </div>
  </section>

  <section class="card card--back" aria-label="Business card back">
    <svg class="card__edge" viewBox="0 0 503 325" preserveAspectRatio="none" aria-hidden="true">
      <path fill="var(--brick)" d="M0,0 L503,0 L503,160 L488,164 L470,158 L452,166 L434,160 L414,168 L396,162 L378,170 L358,164 L340,172 L320,166 L300,174 L280,168 L262,176 L244,170 L226,178 L206,172 L188,176 L168,170 L150,178 L130,172 L112,176 L92,170 L74,178 L56,172 L38,180 L20,174 L0,180 Z"/>
    </svg>
    <div class="services">
      <p>Exterior Painting , Interior Painting</p>
      <p>Carpentry , Drywall</p>
    </div>
    <p class="website">BrightwellPainting.com</p>
    <div class="memberships" aria-label="Membership badges">
      <svg class="badge" width="38" height="62" aria-hidden="true"><rect width="38" height="62" rx="3" fill="var(--badge-blue)"/></svg>
      <svg class="badge" width="44" height="36" aria-hidden="true"><rect width="44" height="36" fill="var(--badge-red)"/></svg>
      <svg class="badge" width="80" height="26" aria-hidden="true"><rect width="80" height="26" fill="var(--badge-blue)"/></svg>
      <svg class="badge" width="68" height="28" aria-hidden="true"><rect x="1" y="1" width="66" height="26" fill="none" stroke="var(--badge-grey)" stroke-width="2"/></svg>
      <svg class="badge" width="54" height="50" aria-hidden="true"><circle cx="27" cy="25" r="24" fill="var(--badge-blue)"/></svg>
      <svg class="badge" width="32" height="46" aria-hidden="true"><rect width="32" height="46" fill="var(--badge-grey)"/></svg>
    </div>
  </section>

</main>
</body>
</html>
```